Somebody commencing retirement at age 67 and wanting a card to introduce myself

Something that depicts the activities I intend to pursue in retirement: Travel, Golf (both in Australia and internationally), wining (red) and dining and generally leading a decadent lifestyle with my wife (or by myself as appropriate).

I offer no services, but intend to have a decadent, relaxing
retirement, playing golf, drinking red wine and dining at good
restaurants!

The card needs to have a suitably designed logo that reflects the
foregoing.

Requirements
Must have
• On the front of the card, my photograph (attached and cropped as
• appropriate), my name (Neil Corbishley), my mobile phone number (+61 417
• 382 514), my email address (neil@corbishley.net.au) and my residential
• address (41 Marlowvale Road, Kestrelton, Western Australia 6187,
• Australia).
• The rear of the card should have my postal address (Neil Corbishley
• Post Office Box 418 Brindlecove Western Australia 6951, Australia.)._

```html
<!DOCTYPE html>
<html lang="en">
<head>
<meta charset="utf-8">
<title>Neil Corbishley – Business Card</title>
<link href="https://fonts.googleapis.com/css2?family=Cinzel:wght@500;700&family=Roboto:wght@400&display=swap" rel="stylesheet">
<style>
  :root {
    --bg: #2b2b2d;
    --card-dark: #1f1c1d;
    --card-dark-2: #2c2829;
    --red: #e3222b;
    --white: #ffffff;
    --blue: #1aa3e0;
    --purple: #5b4a7e;
    --photo-1: #3a3f4d;
    --photo-2: #161a24;
  }
  html, body {
    margin: 0;
    width: 1200px;
    height: 906px;
    overflow: hidden;
    background: var(--bg);
  }
  .canvas { position: relative; width: 1200px; height: 906px; }
  .card {
    position: absolute;
    width: 640px;
    height: 366px;
    border-radius: 22px;
    overflow: hidden;
    box-shadow: 0 14px 30px rgba(0,0,0,.5);
  }
  .card--back {
    left: 70px; top: 70px;
    background: linear-gradient(135deg, var(--card-dark-2), var(--card-dark));
  }
  .card--front { left: 490px; top: 470px; background: var(--card-dark); }

  .brand-mark {
    position: absolute;
    width: 120px; height: 120px;
    border-radius: 50%;
    background: var(--white);
    border: 6px solid var(--purple);
    box-sizing: border-box;
    display: flex; align-items: center; justify-content: center;
    text-align: center;
    font-family: "Cinzel", serif;
    font-weight: 700;
    font-size: 15px;
    line-height: 1.25;
    color: var(--card-dark);
    z-index: 2;
  }
  .card--back .brand-mark { left: 260px; top: 58px; }
  .card--front .brand-mark { left: 462px; top: 18px; }

  .back-name {
    position: absolute; left: 0; right: 0; top: 206px;
    text-align: center;
    font-family: "Cinzel", serif; font-weight: 500;
    font-size: 30px; letter-spacing: 2px;
    color: var(--white); margin: 0;
  }
  .back-postal {
    position: absolute; left: 0; right: 0; top: 258px;
    text-align: center;
    font-family: "Cinzel", serif; font-weight: 500;
    font-size: 13.5px; letter-spacing: .5px;
    color: var(--blue); margin: 0;
  }

  .front-bands { position: absolute; inset: 0; }
  .front-name {
    position: absolute; left: 190px; top: 113px;
    margin: 0;
    font-family: "Cinzel", serif; font-weight: 500;
    font-size: 22px; line-height: 30px; letter-spacing: 1.5px;
    color: var(--white);
    transform: rotate(-8.9deg);
    transform-origin: left center;
    white-space: nowrap;
  }
  .photo-slot {
    position: absolute; left: 40px; top: 156px;
    width: 230px; height: 210px;
    background: linear-gradient(180deg, var(--photo-1), var(--photo-2));
  }
  .contact-list {
    position: absolute; right: 26px; top: 206px;
    margin: 0; padding: 0; list-style: none;
    font-family: "Roboto", sans-serif; font-size: 15px;
    color: var(--white); text-align: right; line-height: 24px;
  }
  .contact-list li { display: flex; justify-content: flex-end; align-items: center; gap: 10px; }
  .contact-list .icon { width: 16px; height: 16px; flex: none; }
  .contact-list .icon--none { visibility: hidden; }
</style>
</head>
<body>
<div class="canvas">

  <section class="card card--back" aria-label="Card back">
    <div class="brand-mark">Corbishley<br>Leisure</div>
    <h2 class="back-name">NEIL CORBISHLEY</h2>
    <p class="back-postal">POST OFFICE BOX 418 BRINDLECOVE WESTERN AUSTRALIA 6951, AUSTRALIA</p>
  </section>

  <section class="card card--front" aria-label="Card front">
    <svg class="front-bands" width="640" height="366" viewBox="0 0 640 366" aria-hidden="true">
      <polygon points="0,0 640,0 640,20 0,120" fill="var(--white)"/>
      <polygon points="0,120 640,20 640,95 0,195" fill="var(--red)"/>
    </svg>
    <div class="brand-mark">Corbishley<br>Leisure</div>
    <h1 class="front-name">NEIL CORBISHLEY</h1>
    <div class="photo-slot" role="img" aria-label="Portrait photograph of Neil Corbishley in a dark suit, arms folded"></div>
    <ul class="contact-list">
      <li>+61 417 382 514
        <svg class="icon" viewBox="0 0 16 16"><path d="M4 1l3 3-2 2c1 2 3 4 5 5l2-2 3 3-2 3C7 14 2 9 1 4z" fill="var(--red)"/></svg>
      </li>
      <li>neil@corbishley.net.au
        <svg class="icon" viewBox="0 0 16 16"><rect x="1" y="3" width="14" height="10" fill="var(--red)"/><path d="M1 3l7 6 7-6" fill="none" stroke="var(--card-dark)" stroke-width="1.4"/></svg>
      </li>
      <li>41 Marlowvale Road, Kestrelton
        <svg class="icon" viewBox="0 0 16 16"><path d="M8 1a5 5 0 0 1 5 5c0 4-5 9-5 9S3 10 3 6a5 5 0 0 1 5-5z" fill="var(--red)"/><circle cx="8" cy="6" r="2" fill="var(--card-dark)"/></svg>
      </li>
      <li>Western Australia 6187, Australia<span class="icon icon--none"></span></li>
    </ul>
  </section>

</div>
</body>
</html>
```